Business card design needed for Automotive Reconditioning business

I have a logo design i just cant decide on the best color or layout for the business card, I will upload all the files so you can see all colors schemes we are considering. I have other file formats if needed let me know.

Target Market(s)

automotive dealerships

Contact Information for Business Card

HERE are the Descriptions and info needed on the card:
Interior Repair: Leather carpet burns panels dash Deoderize
Dealer products and Vin Verify
( spot for name and cell number) My name is Norman Bexley phone 614 352-4180 Title COO www.QuorvalMotive.com

Font styles to use
Sans Serif
Other font styles liked:
• what ever you think looks best

Requirements
Must have
• Must be able to change the name and phone for employees

```html
<!DOCTYPE html>
<html lang="en">
<head>
<meta charset="utf-8">
<title>Quorval Auto Reconditioning Corp. – Business Card</title>
<link rel="stylesheet" href="https://fonts.googleapis.com/css2?family=Bebas+Neue&display=swap">
<style>
  :root {
    --card-black: #141414;
    --card-green: #88f000;
    --ink-white: #ffffff;
    --ink-black: #111111;
  }
  * { margin: 0; padding: 0; box-sizing: border-box; }
  html, body {
    width: 1200px;
    height: 686px;
    overflow: hidden;
    background: var(--card-black);
  }
  .card {
    position: relative;
    width: 1200px;
    height: 686px;
    font-family: "Bebas Neue", "Arial Narrow", sans-serif;
    text-transform: uppercase;
    background: var(--card-black);
  }
  .card__top {
    position: absolute;
    left: 0; top: 0;
    width: 1200px;
    height: 474px;
    background: var(--card-black);
  }
  .brand {
    position: absolute;
    left: 100px;
    top: 140px;
    display: flex;
    align-items: center;
    gap: 14px;
  }
  .brand__square {
    width: 22px;
    height: 22px;
    background: var(--card-green);
    flex: none;
  }
  .brand__name {
    color: var(--ink-white);
    font-size: 34px;
    line-height: 1.05;
    letter-spacing: 1px;
  }
  .contact {
    position: absolute;
    left: 590px;
    top: 86px;
    width: 580px;
    text-align: center;
    color: var(--ink-white);
    font-size: 66px;
    line-height: 76px;
    letter-spacing: 0.5px;
  }
  .card__band {
    position: absolute;
    left: 0; top: 474px;
    width: 1200px;
    height: 212px;
    background: var(--card-green);
    color: var(--ink-black);
    padding: 28px 0 0 21px;
  }
  .services__heading {
    font-size: 58px;
    line-height: 62px;
    font-weight: 400;
  }
  .services__list {
    list-style: none;
    font-size: 41px;
    line-height: 60px;
    letter-spacing: 0.3px;
  }
</style>
</head>
<body>
  <main class="card">
    <section class="card__top">
      <div class="brand">
        <span class="brand__square"></span>
        <span class="brand__name">Quorval Auto<br>Reconditioning Corp.</span>
      </div>
      <div class="contact">
        <p class="contact__name">My name is Norman Bexley</p>
        <p class="contact__title">Title: COO</p>
        <p class="contact__phone">(614) 352-4180</p>
      </div>
    </section>
    <section class="card__band services">
      <h2 class="services__heading">Interior Repair:</h2>
      <ul class="services__list">
        <li>Leather, carpet burns, panels, dash, and deorderizer.</li>
        <li>Dealer products, and VIN verify.</li>
      </ul>
    </section>
  </main>
</body>
</html>
```